Day of the Lord Infographic

I would like an infographic, which will be placed on a website. If different sections could be clickable that would be great. I have included a picture file to understand the basic flow and layout Since this will be on a website the image can be longer than a standard 8x11, in fact, that is preferred.
The graphic should be in about the same layout just much nicer. This is indicating that these events will all occur on what is the Day of the Lord in the order that they are laid out in the picture. I don't necessarily need lines except the 5 dotted or dashed lines (might have to enlarge picture)
Maybe the Day of the Lord is a title or on the side.
Next I have included an RTF file that has the information of the notes for each section. These are scripture verses that need to somehow be incorporated. If a clickable option is available then I can set these up on the website, if not then these need to somehow need to be incorporated.
This project is for the education ministry on www.lanternbrookhall.org. Colors can be complementary or coordinating.

```html
<!DOCTYPE html>
<html lang="en">
<head>
<meta charset="utf-8">
<title>Day of the Lord – Year of Recompense</title>
<link href="https://fonts.googleapis.com/css2?family=Roboto:wght@400;500;700;900&display=swap" rel="stylesheet">
<style>
  :root{
    --backdrop:#333333;
    --page:#f4f5f5;
    --teal:#00b3b3;
    --teal-light:#6dd3cf;
    --ink:#111111;
    --line:#1a1a1a;
    --white:#ffffff;
    --shade:#8a8f8f;
  }
  *{box-sizing:border-box;margin:0;padding:0}
  html,body{width:1200px;height:1200px;overflow:hidden;background:var(--backdrop);font-family:"Roboto",sans-serif}
  .sheet{position:absolute;left:191px;top:39px;width:817px;height:1124px;background:var(--page)}
  .connectors{position:absolute;left:0;top:0;width:817px;height:1124px}
  .connectors path{fill:none;stroke:var(--line);stroke-width:1.6}
  .connectors .dotted{stroke-dasharray:2 4}

  .banner-tab{position:absolute;left:548px;top:4px;width:269px;height:50px;background:var(--teal);
    clip-path:polygon(0 0,100% 0,100% 100%,9% 100%);
    box-shadow:-3px 3px 0 var(--shade)}
  .banner-shadow{position:absolute;left:545px;top:7px;width:269px;height:50px;background:var(--shade);
    clip-path:polygon(0 0,100% 0,100% 100%,9% 100%)}
  .banner-title{position:absolute;right:14px;top:2px;color:var(--white);font-weight:900;font-size:34px;letter-spacing:-.3px;line-height:44px}
  .banner-sub{position:absolute;left:627px;top:48px;width:190px;height:24px;background:var(--white);
    border:2px solid var(--teal);border-right:none;clip-path:polygon(0 0,100% 0,100% 100%,8% 100%);
    color:var(--ink);font-weight:700;font-size:16px;line-height:20px;text-align:right;padding-right:13px}

  .event{position:absolute;background:var(--teal);border-radius:6px;color:var(--ink);padding:5px 7px;
    box-shadow:2px 2px 0 var(--page),3.5px 3.5px 0 var(--teal)}
  .event a{color:inherit;text-decoration:none;display:block}
  .event-title{font-size:14px;line-height:15.5px;font-weight:400;color:#0d0d0d}
  .event-refs{font-size:11px;line-height:15px;color:var(--white);margin-top:2px}

  .hub{position:absolute;left:20px;top:460px;width:146px;height:223px;background:var(--teal);border-radius:7px;
    padding:6px 6px;box-shadow:2px 2px 0 var(--page),3.5px 3.5px 0 var(--teal);text-align:center}
  .hub-tag{background:var(--teal-light);color:var(--white);font-weight:700;font-size:16.5px;line-height:22px;border-radius:4px}
  .hub-title{font-weight:700;font-size:21px;line-height:21px;color:var(--ink);margin-top:5px}
  .hub-refs{font-size:11px;line-height:15.4px;color:var(--white);text-align:justify;margin-top:4px}
</style>
</head>
<body>
<main class="sheet">
  <div class="banner-shadow"></div>
  <div class="banner-tab"><span class="banner-title">Day of the Lord</span></div>
  <div class="banner-sub">Year of Recompense</div>

  <svg class="connectors" viewBox="0 0 817 1124" aria-hidden="true">
    <defs>
      <marker id="arrow" viewBox="0 0 10 10" refX="9" refY="5" markerWidth="7" markerHeight="7" orient="auto-start-reverse">
        <path d="M0 0 L10 5 L0 10 L3 5 Z" fill="#1a1a1a" stroke="none"/>
      </marker>
    </defs>
    <path d="M80 452 V116 Q80 96 100 96 H206" marker-end="url(#arrow)"/>
    <path d="M123 452 V286 Q123 266 143 266 H206" marker-end="url(#arrow)"/>
    <path d="M173 488 H206" marker-end="url(#arrow)"/>
    <path d="M173 660 H206" marker-end="url(#arrow)"/>
    <path d="M121 692 V837 Q121 857 141 857 H206" marker-end="url(#arrow)"/>
    <path d="M79 692 V997 Q79 1017 99 1017 H206" marker-end="url(#arrow)"/>

    <path d="M288 250 V222 Q288 202 308 202 H374" marker-end="url(#arrow)"/>
    <path d="M304 249 Q304 239 318 239 H374" marker-end="url(#arrow)"/>
    <path d="M334 293 H374" marker-end="url(#arrow)"/>
    <path d="M304 334 Q304 345 318 345 H374" marker-end="url(#arrow)"/>
    <path class="dotted" d="M288 334 V370 Q288 381 300 381 H374" marker-end="url(#arrow)"/>
    <path d="M588 292 H641" marker-end="url(#arrow)"/>
    <path d="M719 327 V405 Q719 419 705 419 H302 Q288 419 288 433 V461" marker-end="url(#arrow)"/>
    <path d="M781 443 Q799 443 799 425 V253 Q799 239 785 239 H562" marker-end="url(#arrow)"/>

    <path d="M306 464 Q306 443 320 443 H374" marker-end="url(#arrow)"/>
    <path d="M306 519 Q306 539 320 539 H374" marker-end="url(#arrow)"/>
    <path d="M544 443 H641" marker-end="url(#arrow)"/>
    <path d="M479 576 V593 Q479 607 465 607 H302 Q288 607 288 621 V640" marker-end="url(#arrow)"/>

    <path d="M352 660 H377" marker-end="url(#arrow)"/>
    <path d="M288 748 V826" marker-end="url(#arrow)"/>
    <path d="M288 995 Q288 975 302 975 H378" marker-end="url(#arrow)"/>
    <path d="M288 1066 Q288 1086 302 1086 H378" marker-end="url(#arrow)"/>
  </svg>

  <section class="hub">
    <div class="hub-tag">Day of the Lord</div>
    <h1 class="hub-title">Year of Recompense</h1>
    <p class="hub-refs">2 Thess 4:13-5:9, 1 Thess 2:1-12, Isa 13:6,9; Is 34:8; Jer 46:10; Ezek 13:5, 30:3; Joel 1:15, 2:1, 2:11, 2:31, 3:14; Amos 5:18,20 Obad 15; Zeph 1:7,14; Mal 4:5; Acts 2:20,1 Cor 5:5;1 Thess 5:2; 2 Thess 2:2; 2 Pet 3:10 Isa 2-5; Zech 14</p>
  </section>

  <article class="event" style="left:214px;top:83px;width:210px;height:92px"><a href="#clouds">
    <h2 class="event-title">Day of Clouds, Darkness Signs in Heavens</h2>
    <p class="event-refs">Zeph 1:7-15, Isa 13:1-16, Eze 30:1-9, Amos 5:18,20, Joel 2:2, Amos 8:3,9,13, Mat 24:29</p></a></article>

  <article class="event" style="left:383px;top:192px;width:155px;height:35px;padding-top:2px"><a href="#descend">
    <h2 class="event-title">Descend from Heaven</h2>
    <p class="event-refs" style="margin-top:1px">2 Thess 4:13-5:9</p></a></article>

  <article class="event" style="left:383px;top:232px;width:169px;height:35px;padding-top:2px"><a href="#clouds-coming">
    <h2 class="event-title">Comes in/on the Clouds</h2>
    <p class="event-refs" style="margin-top:1px">Matthew 24:30-31</p></a></article>

  <article class="event" style="left:383px;top:271px;width:199px;height:53px;padding-top:2px"><a href="#voice">
    <h2 class="event-title">Voice of Command to Angels to Gather Elect</h2>
    <p class="event-refs" style="margin-top:1px">1 thess 4:13-5:9, Mat 24:30-31</p></a></article>

  <article class="event" style="left:383px;top:330px;width:247px;height:35px;padding-top:2px"><a href="#trumpet">
    <h2 class="event-title">Trumpet of God(last)</h2>
    <p class="event-refs" style="margin-top:1px">2 Thess 4:13-5:9, Matt 24:30-31, 1 Cor 15(52)</p></a></article>

  <article class="event" style="left:383px;top:369px;width:202px;height:35px;padding-top:2px"><a href="#olives">
    <h2 class="event-title">Will Stand on Mount of Olives</h2>
    <p class="event-refs" style="margin-top:1px">Zech 14:2</p></a></article>

  <article class="event" style="left:214px;top:255px;width:116px;height:76px"><a href="#second-coming">
    <h2 class="event-title">Second Coming Christ</h2>
    <p class="event-refs">2 thess 4:13-5:9, 1 Thess 2:1-12</p></a></article>

  <article class="event" style="left:648px;top:279px;width:137px;height:39px;padding-top:3px"><a href="#angels">
    <h2 class="event-title">Angels Gather Elect</h2>
    <p class="event-refs">Mat 24:30-31</p></a></article>

  <article class="event" style="left:214px;top:469px;width:118px;height:43px"><a href="#rapture">
    <h2 class="event-title">Rapture of Elect</h2>
    <p class="event-refs">1 Thess 4:13-17</p></a></article>

  <article class="event" style="left:383px;top:432px;width:155px;height:71px;padding-top:3px"><a href="#resurrection">
    <h2 class="event-title">Resurrection Dead, Transformation Living into New Bodies</h2>
    <p class="event-refs">1 Cor 15 (23, 51-52)</p></a></article>

  <article class="event" style="left:648px;top:432px;width:122px;height:55px;padding-top:3px"><a href="#meet">
    <h2 class="event-title">Meet Jesus in Clouds, in the Air</h2>
    <p class="event-refs">2 Thess 4:13-5:9</p></a></article>

  <article class="event" style="left:383px;top:527px;width:190px;height:40px;padding-top:3px"><a href="#protects">
    <h2 class="event-title">Protects from Wrath of God</h2>
    <p class="event-refs">2 Thess 4:13-5:9, Zeph 2:3</p></a></article>

  <article class="event" style="left:214px;top:647px;width:135px;height:91px"><a href="#wrath">
    <h2 class="event-title">Wrath of God<br>Day of Destruction</h2>
    <p class="event-refs">Zeph 1:7-15, Isa 13:1-16, Joel 1:15, Isa 34:1-9</p></a></article>

  <article class="event" style="left:383px;top:643px;width:190px;height:35px;padding-top:9px"><a href="#bowls">
    <h2 class="event-title">7 Bowls of Wrath</h2></a></article>

  <article class="event" style="left:214px;top:846px;width:145px;height:75px"><a href="#battle">
    <h2 class="event-title">Day of Battle</h2>
    <p class="event-refs">Mal 4(5), Isa 13:1-16, Joel 2:2-11, Zech 14:3, 5, Isa 13:4</p></a></article>

  <article class="event" style="left:383px;top:958px;width:240px;height:37px;padding-top:3px"><a href="#nations">
    <h2 class="event-title">Nations</h2>
    <p class="event-refs">Eze 30:1-9, Obd, Zeph 1, Isa 34:1-9, Zech 14</p></a></article>

  <article class="event" style="left:214px;top:1002px;width:175px;height:57px;padding-top:3px"><a href="#judgement">
    <h2 class="event-title">Judgement</h2>
    <p class="event-refs">Mal 4:5, Isa 13:1-16, Eze 30:1-9, Obd 15, Isa 4:4, 2 Pet 3:10</p></a></article>

  <article class="event" style="left:383px;top:1069px;width:157px;height:36px;padding-top:3px"><a href="#jehoshaphat">
    <h2 class="event-title">Valley of Jehoshaphat</h2>
    <p class="event-refs">Joel 3:12</p></a></article>
</main>
</body>
</html>
```